Header and footer for report

We would like a header and footer for our building management reports that incorporate a modern city skyline and our logo.

As well as update our other stationery.

```html
<!DOCTYPE html>
<html lang="en">
<head>
<meta charset="utf-8">
<title>Kestrel Group — Stationery</title>
<link href="https://fonts.googleapis.com/css2?family=Open+Sans:wght@400;600;700&display=swap" rel="stylesheet">
<style>
:root{
  --bg:#e9e9ea;
  --paper:#f3f3f3;
  --paper-edge:#dcdcdc;
  --brand-blue:#2e69a6;
  --ink:#1c1d20;
  --text:#55585c;
  --photo-sky:#8f86a3;
  --photo-ground:#3a3a3e;
}
*{margin:0;padding:0;box-sizing:border-box}
html,body{width:1200px;height:795px;overflow:hidden;background:var(--bg);font-family:"Open Sans",Arial,sans-serif;color:var(--text)}
.canvas{position:relative;width:1200px;height:795px}
.sheet{position:absolute;background:var(--paper);box-shadow:0 1px 3px rgba(0,0,0,.12)}
.brand-name{font-family:"Open Sans",Arial,sans-serif;font-weight:700;color:var(--brand-blue);letter-spacing:.02em;white-space:nowrap}
.footer-band{position:absolute;left:0;right:0;bottom:0;display:block}
.icon{display:inline-block;vertical-align:middle;margin-right:2px}

/* letterhead */
.letterhead{left:292px;top:99px;width:293px;height:415px}
.letterhead .brand-name{position:absolute;left:31px;top:60px;font-size:11px}
.letter-body{position:absolute;left:32px;top:106px;width:231px;font-size:4.9px;line-height:7.6px}
.letter-body p{margin-bottom:7.6px;text-align:justify}
.contact-row{position:absolute;display:flex;justify-content:space-between;font-size:5.6px;line-height:7.4px;color:var(--text)}
.letterhead .contact-row{left:32px;right:30px;top:381px}
.contact-address{text-align:right}

/* report cover */
.report-cover{left:636px;top:80px;width:347px;height:437px}
.cover-spine{position:absolute;left:6px;top:0;bottom:0;width:14px;border-left:1px solid var(--paper-edge);border-right:1px solid var(--paper-edge)}
.report-cover .brand-name{position:absolute;left:0;right:0;top:76px;text-align:center;font-size:18px}
.cover-photo{position:absolute;left:0;right:2px;top:124px;height:232px;background:linear-gradient(180deg,var(--photo-sky) 0%,#a89cae 45%,#5c5a60 72%,var(--photo-ground) 100%)}
.cover-footer{position:absolute;left:0;right:0;top:385px;text-align:center;font-size:7px;line-height:8.4px;color:var(--ink)}
.cover-footer .brand-name{position:static;font-size:6.5px}

/* business cards */
.card-back{left:187px;top:550px;width:133px;height:75px;background:var(--brand-blue)}
.card-front{left:187px;top:646px;width:133px;height:75px}
.card-front .brand-name{position:absolute;right:11px;top:31px;font-size:7.2px}
.card-person{position:absolute;left:11px;top:42px;right:11px}
.card-person .name{font-size:4.4px;font-weight:700;color:var(--brand-blue);line-height:5px}
.card-person .role{font-size:3.3px;font-weight:700;color:var(--ink);display:flex;align-items:center;gap:2px}
.card-person .role::after{content:"";flex:1;height:.5px;background:#999}
.card-details{position:absolute;left:11px;right:11px;top:56px;display:flex;justify-content:space-between;font-size:3.3px;line-height:4.6px}

/* compliment slip */
.slip{left:353px;top:561px;width:329px;height:157px}
.slip .brand-name{position:absolute;left:21px;top:57px;font-size:11.5px}
.slip .contact-row{left:22px;right:22px;top:122px;font-size:6.4px;line-height:8.4px}

/* envelope */
.envelope{left:713px;top:561px;width:329px;height:157px}
.envelope-flap{position:absolute;left:0;top:0;width:329px;height:56px}
.envelope .brand-name{position:absolute;left:0;right:0;top:34px;text-align:center;font-size:9.5px;color:#fff}
</style>
</head>
<body>
<div class="canvas">

  <!-- Letterhead -->
  <section class="sheet letterhead">
    <div class="brand-name">KESTREL GROUP</div>
    <div class="letter-body">
      <p>Dear customer,</p>
      <p>Lorem ipsum dolor sit amet, consectetur adipisicing elit, sed do eiusmod tempor incididunt ut labore et dolore magna aliqua. Ut enim ad minim veniam, quis nostrud exercitation ullamco laboris nisi ut aliquip ex ea commodo consequat. Duis aute irure dolor in reprehenderit in voluptate velit esse cillum dolore eu fugiat nulla pariatur. Excepteur sint occaecat cupidatat non proident, sunt in culpa qui officia deserunt mollit anim id est laborum.</p>
      <p>Lorem ipsum dolor sit amet, consectetur adipisicing elit, sed do eiusmod tempor incididunt ut labore et dolore magna aliqua. Ut enim ad minim veniam, quis nostrud exercitation ullamco laboris nisi ut aliquip ex ea commodo consequat. Duis aute irure dolor in reprehenderit in voluptate velit esse cillum dolore eu fugiat nulla pariatur. Excepteur sint occaecat cupidatat non proident, sunt in culpa qui officia deserunt mollit anim id est laborum.</p>
      <p>Lorem ipsum dolor sit amet, consectetur adipisicing elit, sed do eiusmod tempor incididunt ut labore et dolore magna aliqua. Ut enim ad minim veniam, quis nostrud exercitation ullamco laboris nisi ut aliquip ex ea commodo consequat. Duis aute irure dolor in reprehenderit in voluptate velit esse cillum dolore eu fugiat nulla pariatur. Excepteur sint occaecat cupidatat non proident, sunt in culpa qui officia deserunt mollit anim id est laborum.</p>
      <p>Lorem ipsum dolor sit amet, consectetur adipisicing elit, sed do eiusmod tempor incididunt ut labore et dolore magna aliqua. Ut enim ad minim veniam, quis nostrud exercitation ullamco laboris nisi ut aliquip ex ea commodo consequat. Duis aute irure dolor in reprehenderit.</p>
      <p>Yours Sincerely,</p>
    </div>
    <div class="contact-row">
      <div>
        <div><svg class="icon" width="5" height="5" viewBox="0 0 10 10"><path d="M2 1l2 2-1 1.5c.8 1.5 1.8 2.5 3.3 3.3L7.8 6.8 10 9 8.5 10C4 9.5.5 6 0 1.5z" fill="#2e69a6"/></svg>+61 2 9471 3308</div>
        <div><svg class="icon" width="5" height="5" viewBox="0 0 10 10"><rect x="2" y="0" width="6" height="3" fill="#2e69a6"/><rect x="0" y="3.5" width="10" height="4" fill="#2e69a6"/><rect x="2" y="7" width="6" height="3" fill="#2e69a6"/></svg>+61 2 9471 3309</div>
      </div>
      <div>
        <div><svg class="icon" width="5" height="5" viewBox="0 0 10 8"><rect width="10" height="8" fill="#2e69a6"/><path d="M0 0l5 4 5-4" fill="none" stroke="#fff" stroke-width="1"/></svg>info@kestrelgroup.com.au</div>
        <div><svg class="icon" width="5" height="5" viewBox="0 0 10 10"><circle cx="5" cy="5" r="4.3" fill="none" stroke="#2e69a6" stroke-width="1.2"/><path d="M1 5h8M5 1c-2 2.5-2 5.5 0 8M5 1c2 2.5 2 5.5 0 8" fill="none" stroke="#2e69a6" stroke-width=".8"/></svg>www.kestrelgroup.com.au</div>
      </div>
      <div class="contact-address">14 Harbour View Road<br>Northgate, ON L2K 4P1</div>
    </div>
    <svg class="footer-band" width="293" height="7" viewBox="0 0 293 7" preserveAspectRatio="none">
      <polygon points="0,0 190,0 184,7 0,7" fill="#2e69a6"/>
      <polygon points="193,0 293,0 293,7 187,7" fill="#1c1d20"/>
    </svg>
  </section>

  <!-- Report cover -->
  <section class="sheet report-cover">
    <div class="cover-spine"></div>
    <div class="brand-name">KESTREL GROUP</div>
    <div class="cover-photo" role="img" aria-label="Photograph of a modern multi-storey apartment building with patterned facade screens, lit at dusk"></div>
    <div class="cover-footer">
      <div class="brand-name">KESTREL GROUP</div>
      <div>Suite 8, 17 Wharf Street, Marlow, NSW 2199</div>
      <div>www.kestrelgroup.com.au</div>
    </div>
  </section>

  <!-- Business card back -->
  <section class="sheet card-back" role="img" aria-label="Business card reverse with brand pattern on blue"></section>

  <!-- Business card front -->
  <section class="sheet card-front">
    <div class="brand-name">KESTREL GROUP</div>
    <div class="card-person">
      <div class="name">OWEN HARTLEY</div>
      <div class="role">Managing Director</div>
    </div>
    <div class="card-details">
      <div>
        <div>+61 2 9471 3308</div>
        <div>info@kestrelgroup.com.au</div>
        <div>www.kestrelgroup.com.au</div>
      </div>
      <div class="contact-address">Suite 8 / 17<br>Wharf Street,<br>Marlow, NSW 2199</div>
    </div>
    <svg class="footer-band" width="133" height="3" viewBox="0 0 133 3" preserveAspectRatio="none">
      <polygon points="0,0 82,0 79,3 0,3" fill="#2e69a6"/>
      <polygon points="84,0 133,0 133,3 81,3" fill="#1c1d20"/>
    </svg>
  </section>

  <!-- Compliment slip -->
  <section class="sheet slip">
    <div class="brand-name">KESTREL GROUP</div>
    <div class="contact-row">
      <div>
        <div><svg class="icon" width="6" height="6" viewBox="0 0 10 10"><path d="M2 1l2 2-1 1.5c.8 1.5 1.8 2.5 3.3 3.3L7.8 6.8 10 9 8.5 10C4 9.5.5 6 0 1.5z" fill="#2e69a6"/></svg>+61 2 9471 3308</div>
        <div><svg class="icon" width="6" height="6" viewBox="0 0 10 10"><rect x="2" y="0" width="6" height="3" fill="#2e69a6"/><rect x="0" y="3.5" width="10" height="4" fill="#2e69a6"/><rect x="2" y="7" width="6" height="3" fill="#2e69a6"/></svg>+61 2 9471 3309</div>
      </div>
      <div>
        <div><svg class="icon" width="6" height="5" viewBox="0 0 10 8"><rect width="10" height="8" fill="#2e69a6"/><path d="M0 0l5 4 5-4" fill="none" stroke="#fff" stroke-width="1"/></svg>info@kestrelgroup.com.au</div>
        <div><svg class="icon" width="6" height="6" viewBox="0 0 10 10"><circle cx="5" cy="5" r="4.3" fill="none" stroke="#2e69a6" stroke-width="1.2"/><path d="M1 5h8M5 1c-2 2.5-2 5.5 0 8M5 1c2 2.5 2 5.5 0 8" fill="none" stroke="#2e69a6" stroke-width=".8"/></svg>www.kestrelgroup.com.au</div>
      </div>
      <div class="contact-address">14 Harbour View Road<br>Northgate, ON L2K 4P1</div>
    </div>
    <svg class="footer-band" width="329" height="7" viewBox="0 0 329 7" preserveAspectRatio="none">
      <polygon points="0,0 192,0 186,7 0,7" fill="#2e69a6"/>
      <polygon points="196,0 329,0 329,7 189,7" fill="#1c1d20"/>
    </svg>
  </section>

  <!-- Envelope -->
  <section class="sheet envelope">
    <svg class="envelope-flap" width="329" height="56" viewBox="0 0 329 56">
      <path d="M0 0H329L323 48Q322 55 314 55H15Q7 55 6 48Z" fill="#2e69a6"/>
    </svg>
    <div class="brand-name">KESTREL GROUP</div>
  </section>

</div>
</body>
</html>
```